I already have a logo created by Sketch Harbor that I'm very happy with. I need to spruce up my business card now. Its a double sided card with not much info on it, I like to keep it simple.
Front of card: name, phone # email address, web address. Tag Line "Outsourced Technology Solutions", under that it says Business Voice Services & Electronic Protection.
Rear of Card: Content written inside a "cloud" saying "Cloud Solutions" "Cloud Integrity"

Target Market(s)

Business to Business

Industry/Entity Type

Business

Contact Information for Business Card

We are in the technology field. Providing Telephone systems (hardware), SIP Trunks (dial tone/local/long distance/telephone #'s), LAN (Local Area Network)infrastructure cabling, Data Center solutions and Security Applications (Camera systems, Access Control systems,

Requirements
Must have
• Must have brevity
Should not have
• Clutter and/or too much information

```html
<!DOCTYPE html>
<html lang="en">
<head>
<meta charset="utf-8">
<title>Northline Unified Communications – Business Card</title>
<link href="https://fonts.googleapis.com/css2?family=Montserrat:wght@400;500;700&display=swap" rel="stylesheet">
<style>
  :root {
    --brand-blue: #1d4388;
    --ink-gray: #6d6e71;
    --rule-gray: #9a9b9e;
    --paper: #ffffff;
    --backdrop: #d9dadc;
    --band-shadow: #b9babd;
  }
  * { box-sizing: border-box; margin: 0; padding: 0; }
  html, body { width: 1200px; height: 900px; overflow: hidden; }
  body {
    background: var(--backdrop);
    font-family: "Montserrat", sans-serif;
    position: relative;
  }
  .card {
    position: absolute;
    left: 260px;
    width: 680px;
    height: 390px;
    border-radius: 22px;
    overflow: hidden;
    background: var(--paper);
    box-shadow: 0 6px 18px rgba(0,0,0,0.18);
  }
  .card-back { top: 45px; }
  .card-front { top: 465px; }
  .card-shapes { position: absolute; inset: 0; width: 100%; height: 100%; }

  /* back side */
  .back-wordmark {
    position: absolute;
    left: 0; right: 0; top: 120px;
    text-align: center;
    color: var(--paper);
    font-weight: 700;
    font-size: 40px;
    letter-spacing: 1px;
    line-height: 1.1;
  }
  .back-tagline {
    position: absolute;
    right: 40px; top: 292px;
    color: var(--paper);
    font-weight: 400;
    font-size: 15px;
    letter-spacing: 0.6px;
    text-transform: uppercase;
  }

  /* front side */
  .company {
    position: absolute;
    left: 40px; top: 48px;
  }
  .company-name {
    display: flex;
    align-items: flex-start;
    gap: 10px;
    color: var(--brand-blue);
    font-weight: 700;
    font-size: 21px;
    line-height: 1.0;
  }
  .company-mark {
    width: 16px; height: 16px;
    background: var(--brand-blue);
    margin-top: 3px;
    flex: none;
  }
  .company-suffix { font-weight: 700; }
  .company-tagline {
    margin-top: 6px;
    margin-left: 26px;
    padding-top: 4px;
    border-top: 1px solid var(--rule-gray);
    color: var(--ink-gray);
    font-size: 14px;
    font-weight: 400;
    display: inline-block;
  }
  .person {
    position: absolute;
    right: 40px; top: 62px;
    text-align: right;
  }
  .person-name {
    color: var(--brand-blue);
    font-weight: 700;
    font-size: 28px;
    padding-bottom: 4px;
    border-bottom: 1.5px solid var(--brand-blue);
  }
  .person-title {
    color: var(--ink-gray);
    font-size: 14px;
    margin-top: 2px;
  }
  .cloud-badge {
    position: absolute;
    left: 36px; top: 178px;
    width: 140px; height: 86px;
  }
  .cloud-text {
    position: absolute;
    left: 0; right: 0; top: 36px;
    text-align: center;
    color: var(--paper);
    font-weight: 700;
    font-size: 12px;
    line-height: 1.25;
  }
  .contact-list {
    position: absolute;
    left: 40px; top: 296px;
    list-style: none;
  }
  .contact-item {
    display: flex;
    align-items: center;
    gap: 14px;
    color: var(--ink-gray);
    font-size: 16px;
    line-height: 26px;
  }
  .contact-item svg { width: 13px; height: 13px; flex: none; }
  .contact-strong { color: var(--brand-blue); font-weight: 700; }
</style>
</head>
<body>

<section class="card card-back" aria-label="Card back">
  <svg class="card-shapes" viewBox="0 0 680 390" aria-hidden="true">
    <path d="M0 0 H680 V330 H380 L360 352 H300 V330 H0 Z" fill="var(--brand-blue)"/>
  </svg>
  <div class="back-wordmark">Northline<br>Unified</div>
  <p class="back-tagline">Business Voice Services &amp; Electronic Protection</p>
</section>

<section class="card card-front" aria-label="Card front">
  <svg class="card-shapes" viewBox="0 0 680 390" aria-hidden="true">
    <polygon points="500,245 680,205 680,390 470,390" fill="var(--band-shadow)"/>
    <polygon points="512,232 680,195 680,330 500,330" fill="var(--brand-blue)"/>
    <line x1="40" y1="285" x2="505" y2="285" stroke="var(--brand-blue)" stroke-width="1.5"/>
  </svg>

  <div class="company">
    <div class="company-name">
      <span class="company-mark"></span>
      <span>Northline<br>Unified<br>Communications<span class="company-suffix">, LLC</span></span>
    </div>
    <span class="company-tagline">Outsourced Technology Solutions</span>
  </div>

  <div class="person">
    <div class="person-name">Marlo Feneck</div>
    <div class="person-title">Director</div>
  </div>

  <div class="cloud-badge">
    <svg viewBox="0 0 140 86" width="140" height="86" aria-hidden="true">
      <path d="M22 84 C6 84 0 70 4 58 C8 46 18 42 26 44 C26 26 42 14 58 20 C66 6 88 4 98 18 C112 14 126 26 122 40 C136 44 142 62 132 74 C126 82 118 84 110 84 Z" fill="var(--brand-blue)"/>
    </svg>
    <div class="cloud-text">Cloud Solutions<br>Cloud Integrity</div>
  </div>

  <ul class="contact-list">
    <li class="contact-item">
      <svg viewBox="0 0 24 24" aria-hidden="true"><path d="M6.6 10.8a15.1 15.1 0 0 0 6.6 6.6l2.2-2.2a1 1 0 0 1 1-.25 11.4 11.4 0 0 0 3.6.57 1 1 0 0 1 1 1V20a1 1 0 0 1-1 1A17 17 0 0 1 3 4a1 1 0 0 1 1-1h3.5a1 1 0 0 1 1 1c0 1.25.2 2.45.57 3.57a1 1 0 0 1-.25 1z" fill="var(--brand-blue)"/></svg>
      <span>+330 5182-0934</span>
    </li>
    <li class="contact-item">
      <svg viewBox="0 0 24 24" aria-hidden="true"><rect x="2" y="5" width="20" height="14" rx="1.5" fill="none" stroke="var(--brand-blue)" stroke-width="2.4"/><path d="M2.5 6 L12 13 L21.5 6" fill="none" stroke="var(--brand-blue)" stroke-width="2.4"/></svg>
      <span>info@marlofeneck.com</span>
    </li>
    <li class="contact-item">
      <svg viewBox="0 0 24 24" aria-hidden="true"><circle cx="12" cy="12" r="10" fill="var(--brand-blue)"/><path d="M2 12h20M12 2c3 3 3 17 0 20M12 2c-3 3-3 17 0 20" fill="none" stroke="var(--paper)" stroke-width="1.4"/></svg>
      <span>www.<span class="contact-strong">northlineunified</span>.com</span>
    </li>
  </ul>
</section>

</body>
</html>
```